Briar Vale personal care products line

I need a label design for a line of shampoo, conditioner, beard oil, body butter, massage oil, all containing Hemp oil, All Natural product. No phosphates,
I want the design to feel unisex but want to keep it clean as possible. This is for upscale salons and needs to say on the label professional styling products on the label. Please visit my facebook page www.facebook.com/briarvale to see the description of the product benefits. I am attaching some ideas I like as well as the briar vale logo. I would like to see any color of bottle you best think will suit this product as well as new logo design. I am not set on any of these elements. Just the name Briar Vale.

Project Deadline Extended Reason: I have extended the deadline as I had not filled out the description for the design as it should be. I have also added some features that will define the idea as to what we need. I am open to any desing using Briar Vale. The tag line is not anything I am determined to keep either. Please just be creative and help come up with a great product label for this name and product.Thank you to all ! Added Tuesday, June 2, 2015

Target Market(s)

Salons and upper end market

Industry/Entity Type

Cosmetology

Font styles to use
Serif
Sans Serif

Requirements
Must have
• Logo
Nice to have
• Bottle and packaging ideas on color and shape of bottle

```html
<!DOCTYPE html>
<html lang="en">
<head>
<meta charset="utf-8">
<title>Briar Vale Deep Conditioner – Jar Labels</title>
<link href="https://fonts.googleapis.com/css2?family=Encode+Sans+Condensed:wght@300;400;600&display=swap" rel="stylesheet">
<style>
  :root {
    --canvas: #ffffff;
    --gold-light: #f8f0d2;
    --gold-mid: #c9b483;
    --gold-dark: #8f7a45;
    --plum-jar: #5a1f45;
    --plum-jar-light: #9a7a92;
    --amber-jar: #8a2e0c;
    --amber-jar-light: #c2531f;
    --navy-lid: #172636;
    --navy-lid-light: #5b6878;
    --label-sand: #e3d3a8;
    --label-cream: #f2eee4;
    --brand-green: #007a3a;
    --brand-plum: #7e2272;
    --ink: #2b2b2b;
    --white: #ffffff;
    --leaf-sand: #c4a86e;
    --leaf-cream: #ddcda8;
  }
  * { margin: 0; padding: 0; box-sizing: border-box; }
  html, body { width: 1200px; height: 1000px; overflow: hidden; background: var(--canvas); }
  .canvas { position: relative; width: 1200px; height: 1000px; font-family: "Encode Sans Condensed", "Arial Narrow", sans-serif; }

  .jar { position: absolute; left: 0; width: 1200px; height: 400px; }
  .jar--sand { top: 100px; }
  .jar--cream { top: 550px; }

  .jar__lid {
    position: absolute; left: 276px; top: 2px; width: 648px; height: 112px;
    clip-path: polygon(0.6% 0, 99.4% 0, 100% 100%, 0 100%);
    border-radius: 4px 4px 0 0;
  }
  .jar--sand .jar__lid {
    background: linear-gradient(90deg, #b8a477 0%, #ddd0a8 10%, var(--gold-light) 22%, #e6dab8 35%, var(--gold-mid) 55%, #d9c9a0 70%, #b7a06a 85%, var(--gold-dark) 100%);
  }
  .jar--cream .jar__lid {
    background: linear-gradient(90deg, #5b6a7a 0%, #3a4a5a 10%, #2d3e4e 22%, #33465a 35%, #1b2a3a 55%, #0f1c2a 75%, #26364a 88%, var(--navy-lid-light) 100%);
  }

  .jar__body {
    position: absolute; left: 268px; top: 112px; width: 664px; height: 270px;
    border-radius: 26px;
  }
  .jar--sand .jar__body {
    background: linear-gradient(90deg, var(--plum-jar-light) 0%, var(--plum-jar) 15%, #4a1238 40%, var(--plum-jar) 65%, var(--plum-jar-light) 85%, #6a2c55 100%);
  }
  .jar--cream .jar__body {
    background: linear-gradient(90deg, var(--amber-jar-light) 0%, var(--amber-jar) 18%, #4a0c04 40%, var(--amber-jar) 65%, var(--amber-jar-light) 85%, #7a2408 100%);
  }
  .jar__neck {
    position: absolute; left: 298px; top: 108px; width: 604px; height: 10px;
  }
  .jar--sand .jar__neck { background: #5a2049; }
  .jar--cream .jar__neck { background: #6a1e08; }

  .label { position: absolute; left: 268px; top: 150px; width: 664px; height: 205px; overflow: hidden; }
  .jar--sand .label { background: var(--label-sand); }
  .jar--cream .label { top: 143px; height: 212px; background: var(--label-cream); }

  .label__stripe {
    position: absolute; left: 0; bottom: 6px; width: 100%; height: 10px;
    background: linear-gradient(90deg, #c9a23a, #f6df8a 30%, #d8b24a 55%, #f8e59a 80%, #c9a23a);
  }

  .label__leaf { position: absolute; right: 0; top: 5px; width: 112px; height: 185px; border-radius: 60% 0 0 40%; }
  .jar--sand .label__leaf { background: linear-gradient(160deg, rgba(196,168,110,0.35), rgba(176,146,88,0.8)); }
  .jar--cream .label__leaf { right: 0; width: 130px; background: linear-gradient(160deg, rgba(221,205,168,0.4), var(--leaf-cream)); }

  .brand-mark {
    position: absolute; left: 86px; width: 114px; height: 114px; border-radius: 50%;
    display: flex; align-items: center; justify-content: center;
    color: var(--white); font-weight: 400; font-size: 17px; letter-spacing: 0.5px;
  }
  .jar--sand .brand-mark { top: 140px; background: var(--brand-green); }
  .jar--cream .brand-mark { top: 140px; background: var(--brand-plum); }
  .jar--sand .brand-mark, .jar--cream .brand-mark { margin-top: -140px; top: 140px; }
  .jar--sand .brand-mark { top: 140px; }

  .label__copy { position: absolute; left: 220px; top: 42px; }
  .jar--cream .label__copy { top: 49px; }
  .product-name { font-weight: 300; font-size: 48px; line-height: 48px; letter-spacing: 0.5px; }
  .jar--sand .product-name { color: var(--white); }
  .jar--cream .product-name { color: var(--brand-plum); }
  .product-desc { margin-top: 8px; font-weight: 600; font-size: 12.5px; color: var(--ink); letter-spacing: 0.1px; }
  .product-benefit { margin-top: 4px; font-weight: 300; font-size: 25px; line-height: 28px; color: var(--ink); }
</style>
</head>
<body>
<main class="canvas">

  <section class="jar jar--sand">
    <div class="jar__body"></div>
    <div class="jar__neck"></div>
    <div class="jar__lid"></div>
    <div class="label">
      <div class="label__leaf" role="img" aria-label="Large faint hemp leaf decoration"></div>
      <div class="brand-mark" style="top:140px;">BRIAR VALE</div>
      <div class="label__copy">
        <h1 class="product-name">DEEP CONDITIONER</h1>
        <p class="product-desc">100% NATURAL HEMP DEEP CONDITIONING TREATMENT</p>
        <p class="product-benefit">WITH NOURISHING OMEGA 3 OILS</p>
      </div>
      <div class="label__stripe"></div>
    </div>
  </section>

  <section class="jar jar--cream">
    <div class="jar__body"></div>
    <div class="jar__neck"></div>
    <div class="jar__lid"></div>
    <div class="label">
      <div class="label__leaf" role="img" aria-label="Large faint hemp leaf decoration"></div>
      <div class="brand-mark" style="top:147px;">BRIAR VALE</div>
      <div class="label__copy">
        <h2 class="product-name">DEEP CONDITIONER</h2>
        <p class="product-desc">100% NATURAL HEMP DEEP CONDITIONING TREATMENT</p>
        <p class="product-benefit">WITH NOURISHING OMEGA 3 OILS</p>
      </div>
      <div class="label__stripe"></div>
    </div>
  </section>

</main>
</body>
</html>
```